New B2C website design to help dads be better dads

KinQuest is a website to help dads be the “best dad you can be.”

We require our website to be designed into a PSD format, no coding necessary.

The general concept is a two-page design. The first page is the login page, the second page is the home page. Once at the home page, rather than navigating to and from different pages, the user will push and pull through different visual and functional layers of the hierarchy. In theory, this should add to the user experience by having a visual anchor of where they are (through layered pagination) as well as improving loading times since the new information should only be a delta in data load versus a brand new page load.

The general look-and-feel we are going for is clean, simple, minimal. This means that the winning design will show us a good eye for web-optimized typography, good use of white (negative) space, and good use of a visually pleasing grid.

We require a total of 6 page "views" plus the landing page. We note that many of the views are similar to one another.
Landing page
Milestone view
Task view
Content view, articles
Content view, products
Search view
What's new view

Please review all of the additional information provided as well as the attachments for examples.

We provide the following websites as good references for:

Typography:
http://dorvinlesk.com/journal/

Use of white space:
http://www.quartzheron.com/
http://glenmarrow.com/

Example for “scrolling” page concept as well as good balance of color, typography, and white space:
http://www.tovalumeet.eu/

Please contact us with questions so that we can guide your design effort.
Updates

Hello designers,

The following information is added to help guide the design process:

1.  For the text dialogue below the landing page, please assume the following word count:
"why are we making kin quest?": 250 words
"who are we?" 200 words
"what's the deal with the penguin logo?" 300 words

For the social media links, please see http://www.brimlecrates.com/
Notice the floating "social" bar that is always to the right.  This is the concept we are going for, please try to implement this as you see fit. 

Reason: Final design requests have been sent out to finalist designers, want to give everyone time to do a good job.

Target Market(s)

Fathers of young children ages 0-6 years old.

Industry/Entity Type

Product

Font styles to use
Sans Serif

Requirements
Must have
• Clean lines, minimal design concept

Incorporation of our logo (see attached document)

Header content is static for all views after landing page, see example

This page WILL be responsive, please keep that in mind when designing
The timeline bar should be to the left, with the timeline bar’s “milestones” also being responsive.

Designer is free to suggest font types, but any fonts used must be royalty-free and web-optimized. We request a minimum number of font types as well as fonts that load relatively fast. We reinforce that visually appealing typography is a significant factor in the winning design choice.

While we are not expecting the winning design to include code, please keep in mind that the final implementation needs to be optimized for desktop, tablet, and mobile platforms.

If you are using stock photography that is not generated by you, please provide where/how we can obtain imagery, as well as price.

All custom graphics must be available in original formats; Photoshop/GIMP layered files for layout design, and vector formats for logos, icons and other graphical elements.

Please incorporate “Blue” into design elements as you see fit, as the RGB 67 74 169 Blue is the primary color used in our brand. The complement to this blue is 255 202 0, a brownish orange. Feel free to use this color as well, although please keep it to a lesser amount.

Background color is your choice, do not feel the need to use the grey.
Should not have
• Excessive graphical content such that it affects loading times

Excessive use of too many font types such that it affects loading times

```html
<!DOCTYPE html>
<html lang="en">
<head>
<meta charset="utf-8">
<title>KinQuest – Home</title>
<link href="https://fonts.googleapis.com/css2?family=PT+Sans:wght@400;700&family=PT+Sans+Narrow:wght@700&display=swap" rel="stylesheet">
<style>
:root{
  --brand:#434aa9;
  --brand-dark:#2f3590;
  --accent:#ffca00;
  --flag:#e2566f;
  --page:#f2f2f2;
  --panel:#dedede;
  --card:#ffffff;
  --ink:#333333;
  --muted:#666666;
  --line:#c4c4c4;
  --rule:#b9b9b9;
}
*{box-sizing:border-box;margin:0;padding:0}
html,body{width:1200px;height:4045px;overflow:hidden}
body{position:relative;background:var(--page);font-family:"PT Sans",Arial,sans-serif;color:var(--ink);font-size:13px;line-height:1.35}
.hidden-defs{position:absolute;width:0;height:0}

/* header */
.site-header{position:absolute;left:0;top:0;width:1200px;height:185px;background:#fff;border-bottom:1px solid var(--line)}
.brand{position:absolute;left:22px;top:40px;display:flex;align-items:center;gap:10px}
.brand-dot{width:46px;height:46px;border-radius:50%;background:var(--brand)}
.brand-name{font-weight:700;font-size:24px;color:var(--brand)}
.welcome{position:absolute;left:220px;top:26px;font-family:"PT Sans Narrow",Arial,sans-serif;font-weight:700;font-size:40px;color:#222;letter-spacing:.2px}
.score{position:absolute;left:222px;top:94px;font-size:15px;color:#444}
.score b{color:#222}
.search{position:absolute;left:490px;top:84px;display:flex;gap:14px}
.search-field{width:240px;height:36px;border:1px solid var(--line);background:#fff}
.btn{height:36px;padding:0 20px;background:var(--brand);color:#fff;font-weight:700;font-size:14px;display:flex;align-items:center;border-radius:3px;letter-spacing:.5px}
.account{position:absolute;left:955px;top:94px;font-size:15px;color:#444}
.logout{position:absolute;left:1055px;top:84px}

/* share bar */
.share-bar{position:absolute;left:1145px;top:215px;width:55px;height:260px;background:#fff;border:1px solid var(--line);border-right:0;display:flex;flex-direction:column;align-items:center;padding-top:6px;gap:10px;z-index:3}
.share-bar span{font-size:12px;color:var(--muted)}
.share-dot{width:38px;height:38px;border-radius:50%;background:var(--brand)}

/* timeline */
.timeline{position:absolute;left:58px;top:185px;width:3px;height:3860px;background:var(--rule)}
.flag{position:absolute;left:16px;width:52px;height:56px;background:var(--flag);color:#fff;text-align:center;clip-path:polygon(0 0,100% 0,100% 80%,50% 100%,0 80%);z-index:2}
.flag b{display:block;font-size:22px;line-height:28px;font-family:"PT Sans Narrow",Arial,sans-serif}
.flag small{display:block;font-size:8px;letter-spacing:.5px}

/* sections */
.layer{position:absolute;left:90px;width:1075px;background:var(--panel);border-radius:6px}
.layer-head{position:absolute;left:26px;top:16px;display:flex;align-items:center;gap:10px;font-size:20px;color:#333}
.collapse{width:20px;height:20px;border-radius:50%;background:#fff;border:1px solid var(--line);position:relative}
.collapse::after{content:"";position:absolute;left:5px;top:8px;width:8px;height:2px;background:#555}
.big-title{position:absolute;left:330px;top:12px;font-size:30px;color:#222}
.more{position:absolute;left:50%;bottom:-20px;margin-left:-20px;width:40px;height:40px;border-radius:50%;background:var(--brand);border:3px solid var(--page);display:flex;align-items:center;justify-content:center}

/* checklist */
.checklist{position:absolute;left:28px;background:var(--card);width:270px;padding:18px 22px}
.checklist h3{font-size:17px;color:var(--brand);line-height:1.2;margin-bottom:12px}
.checklist .query{font-size:18px;font-weight:700;color:#222;margin-bottom:14px}
.checklist ul{list-style:none}
.checklist li{display:flex;align-items:center;gap:12px;font-size:14px;color:#444;height:34px}
.box{width:18px;height:18px;border:1px solid #aaa;background:#fff;flex:none;position:relative}
.box svg{position:absolute;left:1px;top:-3px}
.rate{margin-top:22px;display:flex;align-items:center;gap:10px;font-size:13px;font-weight:700}
.comments{margin-top:16px;font-size:13px;font-weight:700}
.comments p{font-weight:400;color:#555;margin-top:4px}

/* sort */
.sort{position:absolute;left:920px;top:46px;font-size:13px;color:#444}
.sort-select{margin-top:4px;width:120px;height:26px;background:#fff;border:1px solid var(--line);display:flex;align-items:center;justify-content:space-between;padding:0 8px;font-size:12px}

/* cards */
.card{position:absolute;width:262px;height:328px;background:var(--card);padding:10px}
.thumb{height:148px;border-radius:2px}
.thumb.cabin{background:linear-gradient(135deg,#3c3a38,#7a6a58 55%,#b9a58c)}
.thumb.stroller{background:linear-gradient(135deg,#e9e7df,#8f8a68 50%,#5b5a42)}
.kind{margin-top:12px;color:var(--brand);font-weight:700;font-size:14px;letter-spacing:.5px}
.rating{display:flex;align-items:center;gap:2px;margin-top:4px;font-size:12px;color:var(--muted)}
.rating .count{margin-left:auto}
.card p{margin-top:10px;font-size:13px;color:#444}

/* article */
.sheet{position:absolute;background:var(--card);padding:22px 26px;font-size:13px;color:#444}
.sheet p{margin-bottom:14px}
.hero{width:170px;height:100px;margin:6px auto 18px;background:linear-gradient(135deg,#3c3a38,#7a6a58 55%,#b9a58c)}
.link{color:var(--brand)}
.reviewer{font-weight:700;color:#333;margin-bottom:2px}
.head-rating{position:absolute;left:870px;top:24px;display:flex;align-items:center;gap:2px;font-size:13px;color:#444}
.head-rating span{margin-left:10px}

/* store */
.stores h4{font-size:22px;color:var(--brand);margin-bottom:8px}
.stores table{width:100%;border-collapse:collapse;font-size:13px}
.stores td{padding:2px 0}
.stores td.price{text-align:right;color:var(--brand);font-weight:700}
.product-shot{height:130px;margin:18px 0 10px;background:linear-gradient(135deg,#e9e7df,#8f8a68 50%,#5b5a42)}
</style>
</head>
<body>

<svg class="hidden-defs" aria-hidden="true">
  <defs>
    <symbol id="star" viewBox="0 0 20 20"><path d="M10 1l2.7 5.8 6.3.7-4.7 4.3 1.3 6.2L10 14.9 4.4 18l1.3-6.2L1 7.5l6.3-.7z" fill="#ffca00"/></symbol>
    <symbol id="star-off" viewBox="0 0 20 20"><path d="M10 1l2.7 5.8 6.3.7-4.7 4.3 1.3 6.2L10 14.9 4.4 18l1.3-6.2L1 7.5l6.3-.7z" fill="#cfcfcf"/></symbol>
    <symbol id="tick" viewBox="0 0 20 20"><path d="M3 10l5 5L18 3" fill="none" stroke="#434aa9" stroke-width="3"/></symbol>
    <symbol id="chev" viewBox="0 0 20 20"><path d="M4 6l6 6 6-6M4 11l6 6 6-6" fill="none" stroke="#fff" stroke-width="2.4"/></symbol>
  </defs>
</svg>

<header class="site-header">
  <div class="brand"><div class="brand-dot"></div><div class="brand-name">KinQuest</div></div>
  <h1 class="welcome">Welcome Greg, what would you like to do today?</h1>
  <div class="score">Super Dad Score: <b>10,500</b></div>
  <div class="search"><div class="search-field"></div><div class="btn">SEARCH</div></div>
  <div class="account">My account</div>
  <div class="btn logout">LOGOUT</div>
</header>

<aside class="share-bar"><span>Share</span><div class="share-dot"></div><div class="share-dot"></div><div class="share-dot"></div><div class="share-dot"></div></aside>

<div class="timeline"></div>

<!-- Layer 0: milestone -->
<div class="flag" style="top:198px"><b>0</b><small>STEP</small></div>
<section class="layer" style="top:195px;height:765px">
  <div class="layer-head"><span class="collapse"></span>Prepare for the baby arrival</div>
  <div class="checklist" style="top:55px">
    <ul>
      <li><span class="box"></span>Buy a crib</li>
      <li><span class="box"></span>Assemble the crib</li>
      <li><span class="box"></span>Buy a stroller</li>
      <li><span class="box"><svg width="18" height="18"><use href="#tick"/></svg></span>Buy a carseat</li>
      <li><span class="box"></span>Install a carseat</li>
      <li><span class="box"></span>Learn to change a diaper</li>
      <li><span class="box"></span>Learn to hold a baby</li>
      <li><span class="box"></span>Set a feeding schedule</li>
    </ul>
  </div>
  <div class="card" style="left:330px;top:48px"><div class="thumb cabin" role="img" aria-label="Dad fitting a baby car seat in the back of a car"></div><div class="kind">ARTICLE</div><div class="rating"><svg width="14" height="14"><use href="#star"/></svg><svg width="14" height="14"><use href="#star"/></svg><svg width="14" height="14"><use href="#star"/></svg><svg width="14" height="14"><use href="#star-off"/></svg><svg width="14" height="14"><use href="#star-off"/></svg><span class="count">3,121 ratings</span></div><p>I went out to buy my first car seat and had to earn my PhD in car seats, Newtonian physics, and anti-stain technology...</p></div>
  <div class="card" style="left:625px;top:48px"><div class="thumb stroller" role="img" aria-label="Olive green stroller and matching infant seat"></div><div class="kind">PRODUCT</div><div class="rating"><svg width="14" height="14"><use href="#star"/></svg><svg width="14" height="14"><use href="#star"/></svg><svg width="14" height="14"><use href="#star"/></svg><svg width="14" height="14"><use href="#star"/></svg><svg width="14" height="14"><use href="#star-off"/></svg><span class="count">9,002 likes</span></div><p>The Trellan XT stroller is this year's hottest stroller, for more reasons than are obvious. What we particularly like about it is...</p></div>
  <div class="card" style="left:330px;top:405px"><div class="thumb cabin" role="img" aria-label="Dad checking the straps of a car seat"></div><div class="kind">ARTICLE</div><div class="rating"><svg width="14" height="14"><use href="#star"/></svg><svg width="14" height="14"><use href="#star"/></svg><svg width="14" height="14"><use href="#star"/></svg><svg width="14" height="14"><use href="#star-off"/></svg><svg width="14" height="14"><use href="#star-off"/></svg><span class="count">1,595 likes</span></div><p>I learned something new this week which made my penny-pinching side just giddy. Car seats double as airplane...</p></div>
  <div class="card" style="left:625px;top:405px"><div class="thumb cabin" role="img" aria-label="Dad packing gear into a car"></div><div class="kind">ARTICLE</div><div class="rating"><svg width="14" height="14"><use href="#star"/></svg><svg width="14" height="14"><use href="#star"/></svg><svg width="14" height="14"><use href="#star"/></svg><svg width="14" height="14"><use href="#star"/></svg><svg width="14" height="14"><use href="#star-off"/></svg><span class="count">9,007 likes</span></div><p>Don't forget your go-bag essentials! Camping gear aside, Trailpack Co. has assembled a great kit to take...</p></div>
  <div class="sort">Sort by:<div class="sort-select">Most recent <span>▾</span></div></div>
  <div class="more"><svg width="20" height="20"><use href="#chev"/></svg></div>
</section>

<!-- Layer 1: article -->
<div class="flag" style="top:998px"><b>1</b><small>STEP</small></div>
<section class="layer" style="top:995px;height:725px">
  <div class="layer-head"><span class="collapse"></span>Prepare for the baby arrival</div>
  <h2 class="big-title">Just Call Me Dr. Car Seat</h2>
  <div class="head-rating"><svg width="16" height="16"><use href="#star"/></svg><svg width="16" height="16"><use href="#star"/></svg><svg width="16" height="16"><use href="#star"/></svg><svg width="16" height="16"><use href="#star-off"/></svg><svg width="16" height="16"><use href="#star-off"/></svg><span>3,121 likes</span></div>
  <div class="checklist" style="top:55px">
    <ul>
      <li><span class="box"></span>Buy a crib</li>
      <li><span class="box"></span>Assemble the crib</li>
      <li><span class="box"></span>Buy a stroller</li>
      <li><span class="box"><svg width="18" height="18"><use href="#tick"/></svg></span>Buy a carseat</li>
      <li><span class="box"></span>Install a carseat</li>
      <li><span class="box"></span>Learn to change a diaper</li>
      <li><span class="box"></span>Learn to hold a baby</li>
      <li><span class="box"></span>Set a feeding schedule</li>
    </ul>
    <div class="rate">Rate this : <span><svg width="15" height="15"><use href="#star"/></svg><svg width="15" height="15"><use href="#star"/></svg><svg width="15" height="15"><use href="#star"/></svg><svg width="15" height="15"><use href="#star-off"/></svg><svg width="15" height="15"><use href="#star-off"/></svg></span></div>
    <div class="comments">Comments:<p>Lorem ipsum dolor sit amet, consectetur adipisicing elit, sed do eiusmod tempor incididunt ut labore et dolore magna aliqua. Ut enim ad minim veniam.</p></div>
  </div>
  <article class="sheet" style="left:315px;top:55px;width:705px;height:635px">
    <p>I went out to buy my first car seat and had to earn my PhD in car seats, Newtonian physics, and anti-stain technology. Lorem ipsum dolor sit amet, consectetur adipisicing elit, sed do eiusmod tempor incididunt ut labore et dolore magna aliqua. Ut enim ad minim veniam, quis nostrud exercitation ullamco laboris nisi ut aliquip ex ea commodo consequat.</p>
    <div class="hero" role="img" aria-label="Dad installing a car seat in the back seat"></div>
    <p>Lorem ipsum dolor sit amet, consectetur adipisicing elit, sed do eiusmod tempor incididunt ut labore et dolore magna aliqua. Ut enim ad minim veniam, quis nostrud exercitation ullamco laboris nisi ut aliquip ex ea commodo consequat. Duis aute irure dolor in reprehenderit in voluptate velit esse cillum dolore eu fugiat nulla pariatur. Excepteur sint occaecat cupidatat non proident, sunt in culpa qui officia deserunt mollit anim id est laborum.</p>
    <p class="link">Follow Dad's Reviews:</p>
    <p><span class="reviewer">DadRidge42:</span><br>Lorem ipsum dolor sit amet, consectetur adipisicing elit, sed do eiusmod tempor incididunt ut labore et dolore magna aliqua.</p>
    <p class="link">152 other Dad's found this review helpful.</p>
    <p><span class="reviewer">DadRidge42:</span><br>Lorem ipsum dolor sit amet, consectetur adipisicing elit, sed do eiusmod tempor incididunt ut labore et dolore magna aliqua.</p>
    <p class="link">105 other Dad's found this review helpful.</p>
  </article>
  <div class="more"><svg width="20" height="20"><use href="#chev"/></svg></div>
</section>

<!-- Layer 2: product -->
<div class="flag" style="top:1788px"><b>2</b><small>STEP</small></div>
<section class="layer" style="top:1785px;height:540px">
  <div class="layer-head"><span class="collapse"></span>Prepare for the baby arrival</div>
  <h2 class="big-title">Trellan XT Stroller</h2>
  <div class="checklist" style="top:55px">
    <ul>
      <li><span class="box"></span>Buy a crib</li>
      <li><span class="box"></span>Assemble the crib</li>
      <li><span class="box"></span>Buy a stroller</li>
      <li><span class="box"><svg width="18" height="18"><use href="#tick"/></svg></span>Buy a carseat</li>
      <li><span class="box"></span>Install a carseat</li>
      <li><span class="box"></span>Learn to change a diaper</li>
      <li><span class="box"></span>Learn to hold a baby</li>
      <li><span class="box"></span>Set a feeding schedule</li>
    </ul>
    <div class="rate">Rate this : <span><svg width="15" height="15"><use href="#star"/></svg><svg width="15" height="15"><use href="#star"/></svg><svg width="15" height="15"><use href="#star"/></svg><svg width="15" height="15"><use href="#star-off"/></svg><svg width="15" height="15"><use href="#star-off"/></svg></span></div>
    <div class="comments">Comments:<p>Lorem ipsum dolor sit amet, consectetur adipisicing elit, sed do eiusmod tempor incididunt ut labore et dolore magna aliqua. Ut enim ad minim veniam.</p></div>
  </div>
  <article class="sheet" style="left:330px;top:55px;width:390px;height:380px">
    <p>The Trellan XT stroller is this year's hottest stroller, for more reasons than are obvious. What we particularly like about it is...</p>
    <p class="link">Follow Dad's Reviews:</p>
    <p><span class="reviewer">DadRidge42:</span><br>Lorem ipsum dolor sit amet, consectetur adipisicing elit, sed do eiusmod tempor incididunt ut labore et dolore magna aliqua.</p>
    <p class="link">152 other Dad's found this review helpful.</p>
    <p><span class="reviewer">DadRidge42:</span><br>Lorem ipsum dolor sit amet, consectetur adipisicing elit, sed do eiusmod tempor incididunt.</p>
    <p class="link">105 other Dad's found this review helpful.</p>
  </article>
  <div class="sheet stores" style="left:740px;top:55px;width:280px;height:345px">
    <h4>Available at:</h4>
    <table>
      <tr><td>Shopmart.com</td><td class="price">$249.95</td></tr>
      <tr><td>Cradle Row</td><td class="price">$258.95</td></tr>
      <tr><td>Tot Harbor</td><td class="price">$277.95</td></tr>
    </table>
    <div class="product-shot" role="img" aria-label="Olive green stroller with infant seat"></div>
    <div class="rating"><svg width="14" height="14"><use href="#star"/></svg><svg width="14" height="14"><use href="#star"/></svg><svg width="14" height="14"><use href="#star"/></svg><svg width="14" height="14"><use href="#star-off"/></svg><svg width="14" height="14"><use href="#star-off"/></svg><span class="count">3,121 likes</span></div>
  </div>
  <div class="more"><svg width="20" height="20"><use href="#chev"/></svg></div>
</section>

<!-- Layer 3: what's new -->
<div class="flag" style="top:2378px"><b>3</b><small>STEP</small></div>
<section class="layer" style="top:2375px;height:825px">
  <div class="layer-head"><span class="collapse"></span>What's the latest?</div>
  <div class="checklist" style="top:55px">
    <h3>Related milestones and tasks include:</h3>
    <ul>
      <li><span class="box"></span>Buy a crib</li>
      <li><span class="box"></span>Assemble the crib</li>
      <li><span class="box"></span>Buy a stroller</li>
      <li><span class="box"><svg width="18" height="18"><use href="#tick"/></svg></span>Buy a carseat</li>
      <li><span class="box"></span>Install a carseat</li>
      <li><span class="box"></span>Learn to change a diaper</li>
      <li><span class="box"></span>Learn to hold a baby</li>
      <li><span class="box"></span>Set a feeding schedule</li>
    </ul>
  </div>
  <div class="card" style="left:330px;top:55px"><div class="thumb cabin" role="img" aria-label="Dad fitting a baby car seat in the back of a car"></div><div class="kind">ARTICLE</div><div class="rating"><svg width="14" height="14"><use href="#star"/></svg><svg width="14" height="14"><use href="#star"/></svg><svg width="14" height="14"><use href="#star"/></svg><svg width="14" height="14"><use href="#star-off"/></svg><svg width="14" height="14"><use href="#star-off"/></svg><span class="count">3,121 ratings</span></div><p>I went out to buy my first car seat and had to earn my PhD in car seats, Newtonian physics, and anti-stain technology...</p></div>
  <div class="card" style="left:625px;top:55px"><div class="thumb stroller" role="img" aria-label="Olive green stroller and matching infant seat"></div><div class="kind">PRODUCT</div><div class="rating"><svg width="14" height="14"><use href="#star"/></svg><svg width="14" height="14"><use href="#star"/></svg><svg width="14" height="14"><use href="#star"/></svg><svg width="14" height="14"><use href="#star"/></svg><svg width="14" height="14"><use href="#star-off"/></svg><span class="count">9,002 likes</span></div><p>The Trellan XT stroller is this year's hottest stroller, for more reasons than are obvious. What we particularly like about it is...</p></div>
  <div class="card" style="left:330px;top:420px"><div class="thumb cabin" role="img" aria-label="Dad checking the straps of a car seat"></div><div class="kind">ARTICLE</div><div class="rating"><svg width="14" height="14"><use href="#star"/></svg><svg width="14" height="14"><use href="#star"/></svg><svg width="14" height="14"><use href="#star"/></svg><svg width="14" height="14"><use href="#star-off"/></svg><svg width="14" height="14"><use href="#star-off"/></svg><span class="count">1,595 likes</span></div><p>I learned something new this week which made my penny-pinching side just giddy. Car seats double as airplane...</p></div>
  <div class="card" style="left:625px;top:420px"><div class="thumb cabin" role="img" aria-label="Dad packing gear into a car"></div><div class="kind">ARTICLE</div><div class="rating"><svg width="14" height="14"><use href="#star"/></svg><svg width="14" height="14"><use href="#star"/></svg><svg width="14" height="14"><use href="#star"/></svg><svg width="14" height="14"><use href="#star"/></svg><svg width="14" height="14"><use href="#star-off"/></svg><span class="count">9,007 likes</span></div><p>Don't forget your go-bag essentials! Camping gear aside, Trailpack Co. has assembled a great kit to take...</p></div>
  <div class="sort">Sort by:<div class="sort-select">Most recent <span>▾</span></div></div>
  <div class="more"><svg width="20" height="20"><use href="#chev"/></svg></div>
</section>

<!-- Layer 4: search -->
<div class="flag" style="top:3238px"><b>4</b><small>STEP</small></div>
<section class="layer" style="top:3235px;height:830px">
  <div class="layer-head"><span class="collapse"></span>What you searched for:</div>
  <div class="checklist" style="top:55px">
    <div class="query">Car seats</div>
    <h3>Milestones and tasks related to your search:</h3>
    <ul>
      <li><span class="box"></span>Buy a crib</li>
      <li><span class="box"></span>Assemble the crib</li>
      <li><span class="box"></span>Buy a stroller</li>
      <li><span class="box"><svg width="18" height="18"><use href="#tick"/></svg></span>Buy a carseat</li>
      <li><span class="box"></span>Install a carseat</li>
      <li><span class="box"></span>Learn to change a diaper</li>
      <li><span class="box"></span>Learn to hold a baby</li>
      <li><span class="box"></span>Set a feeding schedule</li>
    </ul>
  </div>
  <div class="card" style="left:330px;top:55px"><div class="thumb cabin" role="img" aria-label="Dad fitting a baby car seat in the back of a car"></div><div class="kind">ARTICLE</div><div class="rating"><svg width="14" height="14"><use href="#star"/></svg><svg width="14" height="14"><use href="#star"/></svg><svg width="14" height="14"><use href="#star"/></svg><svg width="14" height="14"><use href="#star-off"/></svg><svg width="14" height="14"><use href="#star-off"/></svg><span class="count">3,121 ratings</span></div><p>I went out to buy my first car seat and had to earn my PhD in car seats, Newtonian physics, and anti-stain technology...</p></div>
  <div class="card" style="left:625px;top:55px"><div class="thumb stroller" role="img" aria-label="Olive green stroller and matching infant seat"></div><div class="kind">PRODUCT</div><div class="rating"><svg width="14" height="14"><use href="#star"/></svg><svg width="14" height="14"><use href="#star"/></svg><svg width="14" height="14"><use href="#star"/></svg><svg width="14" height="14"><use href="#star"/></svg><svg width="14" height="14"><use href="#star-off"/></svg><span class="count">9,002 likes</span></div><p>The Trellan XT stroller is this year's hottest stroller, for more reasons than are obvious. What we particularly like about it is...</p></div>
  <div class="card" style="left:330px;top:420px"><div class="thumb cabin" role="img" aria-label="Dad checking the straps of a car seat"></div><div class="kind">ARTICLE</div><div class="rating"><svg width="14" height="14"><use href="#star"/></svg><svg width="14" height="14"><use href="#star"/></svg><svg width="14" height="14"><use href="#star"/></svg><svg width="14" height="14"><use href="#star-off"/></svg><svg width="14" height="14"><use href="#star-off"/></svg><span class="count">1,595 likes</span></div><p>I learned something new this week which made my penny-pinching side just giddy. Car seats double as airplane...</p></div>
  <div class="card" style="left:625px;top:420px"><div class="thumb cabin" role="img" aria-label="Dad packing gear into a car"></div><div class="kind">ARTICLE</div><div class="rating"><svg width="14" height="14"><use href="#star"/></svg><svg width="14" height="14"><use href="#star"/></svg><svg width="14" height="14"><use href="#star"/></svg><svg width="14" height="14"><use href="#star"/></svg><svg width="14" height="14"><use href="#star-off"/></svg><span class="count">9,007 likes</span></div><p>Don't forget your go-bag essentials! Camping gear aside, Trailpack Co. has assembled a great kit to take...</p></div>
  <div class="sort">Sort by:<div class="sort-select">Most recent <span>▾</span></div></div>
</section>

</body>
</html>
```